Old Fashioned, Artisan Goat Milk Soap Label

We are branching out in our goat milk dairy into artisan goat milk soaps. High quality, yet an old fashioned feel. Simple yet elegant. Emphasis on the milk and its moisturizing, healing, softening, and superiority.
Purity in a simple design that harkens back to a quaint, earlier time where quality ingredients were valued as much as quality workmanship.
Perhaps a drop symbolizing the milk, or a bucket pouring into or out of the logo. We already have our farm logo, Willowbrook Hollow, and were thinking the soap would be "Sweet Nell"
The labels will grace our liquid soap bottles and our bar soaps. 3.5" X 2.5"
The label color will be an antiqued ivory or other shade to convey a simpler time.

Reason: Realized that the contest length was short enough to scare away designers. Adding time to give entered designers time to create.

Target Market(s)

Upscale people looking to know where their products come from. People looking for better options, artisan products.

Requirements
Must have
• My project must have emphasis on the milk, old time feel, simple elegance
Nice to have
• Perhaps a drop symbolizing the milk, or a bucket pouring into or out of the logo. We already have our farm logo, Willowbrook Hollow, and were thinking the soap would be "Sweet Nell"
• If you use a goat, please be aware that we have the breed Nubians that have long luxurious ears and don't have horns.

```html
<!DOCTYPE html>
<html lang="en">
<head>
<meta charset="utf-8">
<title>Sweet Nell – Goats Milk Soap Label</title>
<link rel="stylesheet" href="https://fonts.googleapis.com/css2?family=Pinyon+Script&family=Cormorant+SC:wght@500&family=IM+Fell+English+SC&display=swap">
<style>
  :root {
    --ivory: #f8f4dc;
    --frame: #efe6b2;
    --frame-soft: #f2eac0;
    --ink: #1f2148;
    --subtitle: #efe6bd;
    --art-top: #d9d6d2;
    --art-bottom: #8d8ea6;
  }
  html, body {
    margin: 0;
    padding: 0;
    overflow: hidden;
    background: var(--ivory);
  }
  .label {
    position: relative;
    width: 1200px;
    height: 849px;
    background: var(--ivory);
    overflow: hidden;
  }
  .label__frame {
    position: absolute;
    inset: 0;
    width: 1200px;
    height: 849px;
  }
  .label__frame .frame-outer {
    fill: none;
    stroke: var(--frame);
    stroke-width: 6;
  }
  .label__frame .frame-inner {
    fill: none;
    stroke: var(--frame-soft);
    stroke-width: 2.5;
  }
  .label__tagline {
    position: absolute;
    top: 78px;
    left: 0;
    width: 100%;
    text-align: center;
    font-family: "Pinyon Script", cursive;
    font-size: 38px;
    line-height: 1;
    color: var(--ink);
    margin: 0;
  }
  .label__product {
    position: absolute;
    top: 140px;
    left: 0;
    width: 100%;
    text-align: center;
    font-family: "Cormorant SC", serif;
    font-weight: 500;
    font-size: 38px;
    letter-spacing: 6px;
    color: var(--subtitle);
    margin: 0;
  }
  .label__illustration {
    position: absolute;
    left: 490px;
    top: 232px;
    width: 222px;
    height: 352px;
    border-radius: 40% 40% 12px 12px;
    background: linear-gradient(180deg, var(--art-top), var(--art-bottom));
  }
  .label__name {
    position: absolute;
    top: 604px;
    left: 0;
    width: 100%;
    text-align: center;
    font-family: "IM Fell English SC", serif;
    font-size: 66px;
    letter-spacing: 3px;
    line-height: 1;
    color: var(--ink);
    margin: 0;
  }
</style>
</head>
<body>
  <main class="label">
    <svg class="label__frame" viewBox="0 0 1200 849" aria-hidden="true">
      <g>
        <path class="frame-outer" d="M600 38 C480 38 400 48 360 78 L250 78 L250 98 L210 98 Q210 140 170 150 L72 150 L72 700 L170 700 Q210 710 210 752 L250 752 L250 772 L360 772 C400 800 480 810 600 810"/>
        <path class="frame-inner" d="M600 52 C485 52 410 62 368 92 L236 92 L236 112 L222 112 Q216 158 178 164 L86 164 L86 686 L178 686 Q216 692 222 738 L236 738 L236 758 L368 758 C410 788 485 796 600 796"/>
      </g>
      <g transform="translate(1200 0) scale(-1 1)">
        <path class="frame-outer" d="M600 38 C480 38 400 48 360 78 L250 78 L250 98 L210 98 Q210 140 170 150 L72 150 L72 700 L170 700 Q210 710 210 752 L250 752 L250 772 L360 772 C400 800 480 810 600 810"/>
        <path class="frame-inner" d="M600 52 C485 52 410 62 368 92 L236 92 L236 112 L222 112 Q216 158 178 164 L86 164 L86 686 L178 686 Q216 692 222 738 L236 738 L236 758 L368 758 C410 788 485 796 600 796"/>
      </g>
    </svg>

    <p class="label__tagline">Hendmade</p>
    <h2 class="label__product">GOATS MILK SOAP</h2>

    <div class="label__illustration" role="img" aria-label="Engraved illustration of a milkmaid carrying two milk buckets on a shoulder yoke"></div>

    <h1 class="label__name">Sweet Nell</h1>
  </main>
</body>
</html>
```